Business Card design - 2 sides

I need a new business card design using our new branding.
On one side of the card I need to have our logo and my contact details et. On the otherside I need to display an offer to go to our website and order a copy of our free report.
If you visit my website www.kelbrookholdings.com.au you will see our logo and branding colours. You will also see an opt-in box with a picture of our free report and CD.
These are the details I would like on the front of the card
Logo: See attached logo file
Tag line:
Company Name: Kelbrook Holdings Australia
Name: Dennis Halloway
Title: Business Developer
Address:
Level 8, 54 Warrane Lane
Sydney NSW 2000
PO Box 4826 Carrowby Heights
NSW 2187 Australia
Telephone: 1300 418 965
Mobile: 0431 906 273
Facsimile: 1300 418 966
Email: dennis.halloway@kelbrookholdings.com.au
Website: www.kelbrookholdings.com.au
These are the details to go on the backside of the card
Picture of Report and CD (see attached image file)
Offer:
ATTENTION: Importers and Exporters...
REVEALED AT LAST!! The 5 Critical Qualities Your Currency Exchange Provider Must Have!
Claim your complimentary copy of “The Quiet Owner's Handbook on
Lasting Overseas Payment Results”” (valued at $97)
Simply go to www.kelbrookholdings.com.au
Attachments: I have attached
1. PSD file of our Free report
2. PNG file of our logo (Main logo is blue and green lettering: Logo2)
3. PNG file of alternative logo, I'm not sure if this will be needed but included anyway (white and green lettering: Logo3)
Best regards,
Dennis
Business Owners and Financial Controllers of Import/Export companies.
Business

```html
<!DOCTYPE html>
<html lang="en">
<head>
<meta charset="UTF-8">
<title>Kelbrook Holdings Australia – Business Card</title>
<link href="https://fonts.googleapis.com/css2?family=Open+Sans:wght@400;600;700&display=swap" rel="stylesheet">
<style>
  :root {
    --navy: #23357f;
    --green: #9ccb2f;
    --white: #ffffff;
    --metal-light: #f1f1f2;
    --metal-mid: #d6d7d9;
    --metal-dark: #bfc0c3;
    --text-grey: #5a5b5e;
    --page: #e8e8ea;
  }
  * { margin: 0; padding: 0; box-sizing: border-box; }
  html, body {
    width: 1200px; height: 720px; overflow: hidden;
    background: var(--page);
    font-family: "Open Sans", Arial, sans-serif;
  }
  .canvas { position: relative; width: 1200px; height: 720px; }

  .card {
    position: absolute; top: 200px;
    width: 560px; height: 320px; overflow: hidden;
    background: linear-gradient(135deg, var(--metal-light) 0%, var(--metal-mid) 45%, var(--metal-light) 70%, var(--metal-dark) 100%);
    box-shadow: 0 4px 14px rgba(0,0,0,0.18);
  }
  .card--front { left: 27px; }
  .card--back { left: 613px; }

  /* Front */
  .swoosh { position: absolute; inset: 0; width: 560px; height: 320px; }
  .brand {
    position: absolute; left: 28px; top: 26px;
    display: flex; align-items: center; gap: 10px;
  }
  .brand__mark { width: 16px; height: 16px; border-radius: 50%; background: var(--green); flex: none; }
  .brand__name {
    font-size: 27px; font-weight: 600; color: var(--navy);
    line-height: 1.1; width: 270px;
  }
  .person { position: absolute; left: 28px; top: 130px; }
  .person__name { font-size: 15px; font-weight: 700; color: var(--navy); }
  .person__title { font-size: 12.5px; color: var(--green); margin-bottom: 8px; }
  .person__address { font-size: 12.5px; color: var(--text-grey); line-height: 1.4; }

  .contact {
    position: absolute; right: 22px;
    display: flex; align-items: center; justify-content: flex-end; gap: 6px;
    color: var(--white); font-size: 12px; white-space: nowrap;
  }
  .contact svg { width: 12px; height: 12px; fill: var(--white); flex: none; }
  .contact__gap { width: 10px; }
  .contact--phone { top: 104px; }
  .contact--mobile { top: 130px; }
  .contact--email { top: 156px; }
  .contact--web { top: 182px; }
  .contact--postal { top: 262px; }

  /* Back */
  .offer { position: absolute; left: 22px; top: 26px; width: 330px; }
  .offer__label { font-size: 17px; font-weight: 700; color: var(--navy); margin-bottom: 6px; letter-spacing: 0.5px; }
  .band {
    font-size: 12px; line-height: 1.35; padding: 4px 8px; margin-bottom: 7px;
  }
  .band--navy { background: var(--navy); color: var(--white); }
  .band--green { background: var(--green); color: var(--navy); font-weight: 600; }
  .band--attention { width: 290px; }
  .band--claim { padding: 6px 8px; }
  .band--cta { width: 300px; }
  .band strong { font-weight: 700; }

  .report-visual {
    position: absolute; left: 370px; top: 50px; width: 168px; height: 196px;
    background: linear-gradient(160deg, #ffffff 0%, #e4e8ef 55%, #c9d3e6 100%);
    border-top: 10px solid var(--green);
    box-shadow: 0 3px 8px rgba(0,0,0,0.2);
  }
  .report-disc {
    position: absolute; left: 468px; top: 150px; width: 84px; height: 84px; border-radius: 50%;
    background: radial-gradient(circle, var(--metal-mid) 0 10%, #ffffff 12% 70%, #e2e4e8 100%);
    border: 3px solid var(--green);
  }
</style>
</head>
<body>
<main class="canvas">

  <section class="card card--front" aria-label="Business card front">
    <svg class="swoosh" viewBox="0 0 560 320" aria-hidden="true">
      <path d="M0 300 C120 296 190 250 230 180 C270 110 360 70 560 56 L560 320 L0 320 Z" fill="var(--navy)"/>
      <path d="M0 289 C118 285 184 240 222 172 C262 100 356 58 560 44" fill="none" stroke="var(--green)" stroke-width="7"/>
      <path d="M0 309 C124 305 196 262 238 190 C280 120 370 82 560 68" fill="none" stroke="var(--white)" stroke-width="2.5"/>
      <path d="M0 316 C160 318 220 300 260 270" fill="none" stroke="var(--green)" stroke-width="3"/>
    </svg>

    <div class="brand">
      <span class="brand__mark"></span>
      <span class="brand__name">Kelbrook Holdings Australia</span>
    </div>

    <div class="person">
      <p class="person__name">Dennis Halloway</p>
      <p class="person__title">Business Developer</p>
      <p class="person__address">Level 8, 54 Warrane Lane<br>Sydney NSW 2000</p>
    </div>

    <p class="contact contact--phone">
      <svg viewBox="0 0 24 24"><path d="M6.6 10.8a15.1 15.1 0 0 0 6.6 6.6l2.2-2.2a1 1 0 0 1 1-.25 11.4 11.4 0 0 0 3.6.57 1 1 0 0 1 1 1V20a1 1 0 0 1-1 1A17 17 0 0 1 3 4a1 1 0 0 1 1-1h3.5a1 1 0 0 1 1 1c0 1.25.2 2.45.57 3.57a1 1 0 0 1-.25 1z"/></svg>
      1300 418 965
    </p>
    <p class="contact contact--mobile">
      <svg viewBox="0 0 24 24"><path d="M7 1h10a2 2 0 0 1 2 2v18a2 2 0 0 1-2 2H7a2 2 0 0 1-2-2V3a2 2 0 0 1 2-2zm0 3v14h10V4zm5 15.5a1 1 0 1 0 0 2 1 1 0 0 0 0-2z"/></svg>
      0431 906 273
      <span class="contact__gap"></span>
      <svg viewBox="0 0 24 24"><path d="M6 2h9l3 3v5H6zM4 11h16a2 2 0 0 1 2 2v7H2v-7a2 2 0 0 1 2-2zm2 4v2h4v-2z"/></svg>
      1300 418 966
    </p>
    <p class="contact contact--email">
      <svg viewBox="0 0 24 24"><path d="M2 5h20v14H2zm2 2v.5l8 5 8-5V7zm0 3v7h16v-7l-8 5z"/></svg>
      enquiries@kelbrookholdings.com.au
    </p>
    <p class="contact contact--web">
      <svg viewBox="0 0 24 24"><path d="M12 2a10 10 0 1 0 0 20 10 10 0 0 0 0-20zm0 2c.9 0 2.2 1.8 2.8 5H9.2C9.8 5.8 11.1 4 12 4zM4.3 11h4.6a20 20 0 0 0 0 2H4.3a8 8 0 0 1 0-2zm6.6 0h2.2a18 18 0 0 1 0 2h-2.2a18 18 0 0 1 0-2zm4.2 0h4.6a8 8 0 0 1 0 2h-4.6a20 20 0 0 0 0-2zM9.2 15h5.6c-.6 3.2-1.9 5-2.8 5s-2.2-1.8-2.8-5z"/></svg>
      www.kelbrookholdings.com.au
    </p>
    <p class="contact contact--postal">PO Box 4826 Carrowby Heights, NSW 2187 Australia</p>
  </section>

  <section class="card card--back" aria-label="Business card back">
    <div class="offer">
      <p class="offer__label">OFFER</p>
      <p class="band band--navy band--attention">ATTENTION &nbsp;Importers and Exporters...</p>
      <p class="band band--green">REVEALED AT LAST!! &nbsp;The 5 Critical Qualities Your Currency Exchange Provider Must Have!</p>
      <p class="band band--navy band--claim">Claim your complimentary copy of “The Quiet Owner's Handbook on Lasting Overseas Payment Results” (<strong>valued at $97</strong>)</p>
      <p class="band band--navy band--cta">Simply go to <strong>www.kelbrookholdings.com.au</strong></p>
    </div>

    <div class="report-visual" role="img" aria-label="Cover of the free report featuring a smiling businesswoman"></div>
    <div class="report-disc" role="img" aria-label="Companion CD with printed report label"></div>
  </section>

</main>
</body>
</html>
```